DJ company new brochure of services offered

I would like to get a new price sheet made for my company services. Currently it's text only. I would like to add pictures next to each service description also like to add general background colors, and just make it look more attractive overall.

Uplighting - File #4 & file #10
Centerpiece pin-spots - File #15
Wedding Cake Spot - file #13 (can you crop out the logo at the bottom)?
Dance Floor Decal File #5
Gobo Monogram - File # 3
market lighting - file #14
ballroom draping - file #7
Video/projections screens: File #13
Indoor safe sparkler effect (not listed on price sheet yet) File #11
Dancing on a cloud - File #9
Co2 Cannons - File #6

Target Market(s)

bride and grooms

Industry/Entity Type

Entertainment

Font styles to use
Serif

Colors

Designer to choose colors to be used in the design.

Requirements
Must have
• my website is www.brightlinkevents.example
• instagram is: @brightlinkevents.example

```html
<!DOCTYPE html>
<html lang="en">
<head>
<meta charset="utf-8">
<title>Additional Service Add-ons — Price Sheet</title>
<link rel="stylesheet" href="https://fonts.googleapis.com/css2?family=Crimson+Pro:wght@400;500;600&display=swap">
<style>
  :root {
    --ink-dark: #111111;
    --ink-brown: #2e2418;
    --panel: #282828;
    --header-bar: #3a3a3a;
    --paper: #ffffff;
    --text-light: #ffffff;
    --accent-red: #e3262b;
  }
  * { margin: 0; padding: 0; box-sizing: border-box; }
  html, body { width: 848px; height: 1200px; overflow: hidden; background: var(--panel); }
  body { font-family: "Crimson Pro", Georgia, serif; color: var(--text-light); }

  .sheet { position: relative; width: 848px; height: 1200px; overflow: hidden; background: var(--panel); }

  .crowd-band { position: absolute; left: 0; top: 0; width: 848px; height: 48px; }
  .contact { position: absolute; right: 24px; top: 24px; transform: translateY(-50%); font-size: 15px; font-weight: 500; color: var(--ink-brown); line-height: 1; white-space: nowrap; }
  .contact .sep { padding: 0 8px; }

  .title-bar { position: absolute; left: 0; top: 48px; width: 848px; height: 40px; background: var(--paper); }
  .title-bar h1 { position: absolute; left: 28px; top: 20px; transform: translateY(-50%); font-weight: 400; font-size: 23.5px; color: var(--ink-dark); line-height: 1; white-space: nowrap; }

  .service { position: absolute; left: 0; width: 848px; background: var(--panel); overflow: hidden; }
  .service__header { position: absolute; left: 0; top: 0; width: 848px; height: 50px; background: var(--header-bar); }
  .service__photo { position: absolute; left: 0; top: 0; width: 848px; height: 100%; }

  .line { position: absolute; line-height: 1; transform: translateY(-50%); white-space: nowrap; }
  .heading { font-size: 23px; font-weight: 600; }
  .heading .note { font-weight: 400; }
  .item { font-size: 20px; }
  .price { font-size: 18px; }

  .uplighting { top: 88px; height: 240px; }
  .pinspot { top: 328px; height: 238px; }
  .monogram { top: 566px; height: 240px; }
  .floor { top: 806px; height: 240px; }

  .extras { position: absolute; left: 0; top: 1046px; width: 848px; height: 112px; }
  .extras__bg { position: absolute; inset: 0; }
  .extras .price { font-size: 17.5px; }

  .notice { position: absolute; left: 0; top: 1158px; width: 848px; height: 42px; background: var(--accent-red); }
  .notice p { position: absolute; left: 32px; top: 21px; transform: translateY(-50%); font-size: 19.5px; line-height: 1; color: var(--text-light); white-space: nowrap; }
</style>
</head>
<body>
<main class="sheet">

  <svg class="crowd-band" viewBox="0 0 848 48" role="img" aria-label="Photo of a concert crowd with raised hands in golden light">
    <defs>
      <linearGradient id="crowdGold" x1="0" y1="0" x2="0" y2="1">
        <stop offset="0" stop-color="#7d6a44"/>
        <stop offset="0.5" stop-color="#c9b27a"/>
        <stop offset="1" stop-color="#e6d7a6"/>
      </linearGradient>
    </defs>
    <rect width="848" height="48" fill="url(#crowdGold)"/>
  </svg>
  <p class="contact">www.brightlinkevents.example<span class="sep">|</span>@brightlinkevents.example</p>

  <header class="title-bar">
    <h1>Additional Service Add-on : (when booked with DJ package)</h1>
  </header>

  <section class="service uplighting">
    <div class="service__header"></div>
    <svg class="service__photo" viewBox="0 0 848 240" role="img" aria-label="Photo of a reception room with warm amber up-lighting and round tables">
      <defs>
        <linearGradient id="upGlow" x1="0" y1="0" x2="1" y2="1">
          <stop offset="0" stop-color="#c9a08a"/>
          <stop offset="0.5" stop-color="#8a6553"/>
          <stop offset="1" stop-color="#3e2c25"/>
        </linearGradient>
      </defs>
      <polygon points="496,0 848,0 848,240 596,240" fill="url(#upGlow)"/>
    </svg>
    <div class="line heading" style="left:27px; top:22px;">Room up-lighting <span class="note">(color of your choice).</span></div>
    <div class="line item" style="left:26px; top:101px;">20 fixtures (med-large room)</div>
    <div class="line price" style="left:391px; top:106px;">$400</div>
    <div class="line item" style="left:26px; top:140px;">16 fixtures (med-large room)</div>
    <div class="line price" style="left:391px; top:141px;">$350</div>
    <div class="line item" style="left:26px; top:174px;">12 fixtures (small-med room)</div>
    <div class="line price" style="left:391px; top:177px;">$300</div>
  </section>

  <section class="service pinspot">
    <div class="service__header"></div>
    <svg class="service__photo" viewBox="0 0 848 238" role="img" aria-label="Photo of a draped ballroom with pin-spotted floral centerpieces in lavender light">
      <defs>
        <linearGradient id="pinLav" x1="0" y1="0" x2="1" y2="1">
          <stop offset="0" stop-color="#d9c6ea"/>
          <stop offset="0.5" stop-color="#a98bc9"/>
          <stop offset="1" stop-color="#6d5687"/>
        </linearGradient>
      </defs>
      <polygon points="490,0 848,0 848,238 592,238" fill="url(#pinLav)"/>
    </svg>
    <div class="line heading" style="left:30px; top:23px;">Pin spot lighting</div>
    <div class="line item" style="left:29px; top:118px;">Wedding cake</div>
    <div class="line item" style="left:29px; top:138px;">Centerpieces</div>
    <div class="line item" style="left:29px; top:159px;">Sweetheart table / etc.</div>
    <div class="line price" style="left:392px; top:136px;">$30+</div>
  </section>

  <section class="service monogram">
    <div class="service__header"></div>
    <svg class="service__photo" viewBox="0 0 848 240" role="img" aria-label="Photo of a sweetheart table and a dance floor with a projected monogram in pink light">
      <defs>
        <linearGradient id="monoPink" x1="0" y1="0" x2="1" y2="1">
          <stop offset="0" stop-color="#8a5d8c"/>
          <stop offset="0.5" stop-color="#d49ed8"/>
          <stop offset="1" stop-color="#f0d4f2"/>
        </linearGradient>
      </defs>
      <polygon points="490,0 848,0 848,240 590,240" fill="url(#monoPink)"/>
    </svg>
    <div class="line heading" style="left:32px; top:24px;">Dance Floor Decal / Gobo Monogram</div>
    <div class="line item" style="left:31px; top:129px;">B&amp;G names appear</div>
    <div class="line item" style="left:31px; top:150px;">onto wall or dance floor</div>
    <div class="line price" style="left:390px; top:138px;">$250+</div>
  </section>

  <section class="service floor">
    <div class="service__header"></div>
    <svg class="service__photo" viewBox="0 0 848 240" role="img" aria-label="Photo of a couple dancing on a white lettered dance floor in a warm ballroom">
      <defs>
        <linearGradient id="floorWarm" x1="0" y1="0" x2="0" y2="1">
          <stop offset="0" stop-color="#5a4534"/>
          <stop offset="0.45" stop-color="#b9a288"/>
          <stop offset="1" stop-color="#eee6dc"/>
        </linearGradient>
      </defs>
      <polygon points="494,0 848,0 848,240 596,240" fill="url(#floorWarm)"/>
    </svg>
    <div class="line heading" style="left:30px; top:24px;">White Dance Floor <span class="note">(Square or Round)</span></div>
    <div class="line price" style="left:234px; top:152px; transform:translate(-50%,-50%);">$1000+</div>
    <div class="line item" style="left:238px; top:169px; transform:translate(-50%,-50%);">(seamless only)</div>
  </section>

  <section class="extras">
    <svg class="extras__bg" viewBox="0 0 848 112" role="img" aria-label="Photo of a dancing crowd with raised hands in dim warm light">
      <defs>
        <linearGradient id="extrasWarm" x1="0" y1="0" x2="1" y2="0">
          <stop offset="0" stop-color="#5a4b3b"/>
          <stop offset="0.5" stop-color="#6e5f4c"/>
          <stop offset="1" stop-color="#3c3128"/>
        </linearGradient>
      </defs>
      <rect width="848" height="112" fill="url(#extrasWarm)"/>
    </svg>
    <div class="line heading" style="left:34px; top:18px;">Dance floor lighting</div>
    <div class="line price" style="left:458px; top:18px;">$200+ (depending on style)</div>
    <div class="line heading" style="left:34px; top:48px;">A/V <span class="note">(screens, projectors, video display)</span></div>
    <div class="line price" style="left:458px; top:46px;">$200+</div>
    <div class="line heading" style="left:33px; top:79px;">String/Bistro Lighting</div>
    <div class="line price" style="left:459px; top:78px;">Depends on size – contact us</div>
  </section>

  <footer class="notice">
    <p>*We offer a wide range of additional services. Please contact us for more info &amp; pricing.</p>
  </footer>

</main>
</body>
</html>
```